Cat-products company needs smart, yet endearing, business card

We need a business card design for a new, but up-and-running, business based in Honolulu, Hawaii. The business is Purrlane Nest Co. Our first product is the most environmentally-friendly cat grass kit ever seen on the planet. Future products, currently in the R&D phase, will include a variety of exciting cat scratchers. We also do consulting work to help apartment-dwellers make their home more cat-friendly and, in the future, plan on doing full, custom installs of structure to create high walkways for cats.

Target Market(s)

Middle-aged, apartment-dwelling, middle-class workers who own 1 or more cats and who dote on them.

Industry/Entity Type

Pet Care

Contact Information for Business Card

A striking, professional, yet warm and friendly design is what we're after.

Font styles to use
Serif
Sans Serif
Other font styles liked:
• Comfortaa

Colors

Designer to choose colors to be used in the design.

Requirements
Must have
• The company logo: (see attachment)
• The company name: Purrlane Nest Co
• The web address: www.purrlanenestco.example
• Email: support@purrlanenestco.example
• Phone: +1 (808) 555 0172
• Update (Fri Jun 30 3017 7:45pm Hawaii Time) I would like, is possible, uploaded picture of the cat grass kit on the back of the card with some text along the lines of: Purrlane Nest Co - Where The Freshest Kitty Sprouts Begin
Nice to have
• A cat picture, cartoon, real or silhouette that illustrates cats in action and/or relaxing; ie using the apartment space to live, play and relax in and being well-contented.
• Most of the website is done in the font: Comfortaa. It might be nice to continue using this for brand consistency.
Should not have
• Hard-to-read fonts.

```html
<!DOCTYPE html>
<html lang="en">
<head>
<meta charset="UTF-8">
<title>Purrlane Nest Co — Business Card</title>
<link href="https://fonts.googleapis.com/css2?family=Comfortaa:wght@400;700&display=swap" rel="stylesheet">
<style>
  :root {
    --paper: #e8e2c4;
    --paper-deep: #ddd6b3;
    --cocoa: #5a3630;
    --leaf: #9ccc3c;
    --leaf-mid: rgba(156, 204, 60, 0.7);
    --leaf-faint: rgba(156, 204, 60, 0);
  }
  * { margin: 0; padding: 0; box-sizing: border-box; }
  html, body {
    width: 1200px;
    height: 686px;
    overflow: hidden;
    background: var(--paper);
  }
  .card {
    position: relative;
    width: 1200px;
    height: 686px;
    background: radial-gradient(ellipse at 40% 40%, var(--paper) 0%, var(--paper-deep) 100%);
    font-family: "Comfortaa", sans-serif;
    color: var(--cocoa);
    overflow: hidden;
  }
  .brand {
    position: absolute;
    left: 180px;
    top: 150px;
    width: 310px;
    text-align: center;
  }
  .brand-mark {
    display: block;
    width: 110px;
    height: 110px;
    margin: 0 auto 40px;
    background: var(--cocoa);
    border-radius: 10px;
  }
  .brand-name {
    font-weight: 700;
    font-size: 54px;
    line-height: 1.08;
    color: var(--leaf);
  }
  .contacts {
    position: absolute;
    left: 616px;
    top: 200px;
    list-style: none;
  }
  .contact {
    display: flex;
    align-items: center;
    height: 34px;
    margin-bottom: 31px;
    font-size: 22px;
    font-weight: 400;
  }
  .contact-icon {
    width: 22px;
    height: 22px;
    margin-right: 16px;
    flex: none;
  }
  .paw-trail {
    position: absolute;
    left: 60px;
    top: 556px;
    width: 830px;
    height: 72px;
    border-radius: 36px;
    background: linear-gradient(90deg, var(--leaf-faint) 0%, rgba(156,204,60,0.35) 45%, rgba(156,204,60,0.55) 100%);
  }
  .cat-figure {
    position: absolute;
    left: 874px;
    top: 390px;
    width: 294px;
    height: 242px;
    border-radius: 46% 54% 38% 42% / 60% 55% 40% 40%;
    background: radial-gradient(ellipse at 35% 55%, var(--leaf) 0%, var(--leaf) 45%, var(--leaf-mid) 70%, var(--leaf-faint) 100%);
  }
  .base-rule {
    position: absolute;
    left: 0;
    top: 660px;
    width: 1200px;
    height: 8px;
    background: var(--cocoa);
  }
</style>
</head>
<body>
<main class="card">
  <section class="brand">
    <span class="brand-mark" aria-hidden="true"></span>
    <h1 class="brand-name">Purrlane<br>Nest Co</h1>
  </section>

  <ul class="contacts">
    <li class="contact">
      <svg class="contact-icon" viewBox="0 0 24 24" aria-hidden="true">
        <g fill="none" stroke="#5a3630" stroke-width="3" stroke-linecap="round">
          <path d="M10 14 L14 10"/>
          <path d="M11 7 L13 5 a4 4 0 0 1 6 6 L17 13"/>
          <path d="M13 17 L11 19 a4 4 0 0 1 -6 -6 L7 11"/>
        </g>
      </svg>
      www.purrlanenestco.example
    </li>
    <li class="contact">
      <svg class="contact-icon" viewBox="0 0 24 24" aria-hidden="true">
        <rect x="2" y="5" width="20" height="14" rx="1.5" fill="#5a3630"/>
        <path d="M3 6 L12 13 L21 6" fill="none" stroke="#e8e2c4" stroke-width="1.6"/>
      </svg>
      support@purrlanenestco.example
    </li>
    <li class="contact">
      <svg class="contact-icon" viewBox="0 0 24 24" aria-hidden="true">
        <path d="M8 2 C5 3 4 6 4 10 C4 15 6 20 9 22 C10 22.5 11 22 11.5 21 L12.5 18 C12.8 17 12.3 16.3 11.5 16 L9.8 15.4 C9 13 9 10.5 9.6 8.5 L11.3 8 C12.1 7.7 12.5 7 12.3 6 L11.5 3 C11.2 2.1 10 1.6 8 2 Z" fill="#5a3630"/>
      </svg>
      +1 (808) 555 0172
    </li>
  </ul>

  <div class="paw-trail" role="img" aria-label="Winding trail of small green cat paw prints growing larger as they lead toward the kitten"></div>
  <div class="cat-figure" role="img" aria-label="Green silhouette of a playful kitten sitting and batting at the air with one raised paw, tail curled up"></div>

  <div class="base-rule" aria-hidden="true"></div>
</main>
</body>
</html>
```